I want a flyer for a company that changes Incandescent bulbs and halogen bulbs in LED. The flyer can content this information and benefits that the LED can “give” you : With the help of LED's you will save up to 90% of the electricity bill, it helps the planet! They don't contain mercury, release carbon dioxide, they resist at lower temperatures, aren't sensitive to humidity, there haven't been any registered case of catching fire, release a bad odor or smoke from them, unlike incandescent and halogen bulbs. Their life spend is higher than 25000 hours! 5 years warranty

Do you want a better life? Do you want to help the planet? Do you want to save money? The LED light bulbs are the solution!
Discover the new and revolutionary way of illuminating your house with the help of LED light bulbs.

These are suggestions, you can do anything you can believe is better, I have no experience in advertising. My supplier is www.glowbarn.co.uk , you can have a look there.

This leaflets will be distributed to the potential customers thru their post boxes.

I want to start the campaign ASAP, so waiting your ideas!!!

```html
<!DOCTYPE html>
<html lang="en">
<head>
<meta charset="utf-8">
<title>Lumera Lighting – LED Flyer</title>
<link href="https://fonts.googleapis.com/css2?family=Teko:wght@400;500;600&family=Lato:wght@700;900&display=swap" rel="stylesheet">
<style>
  :root {
    --orange: #f7870f;
    --orange-deep: #d46a00;
    --charcoal: #3b3b3b;
    --charcoal-dark: #262626;
    --ink: #333333;
    --white: #ffffff;
  }
  * { margin: 0; padding: 0; box-sizing: border-box; }
  html, body { width: 899px; height: 1200px; overflow: hidden; background: var(--charcoal); }
  .flyer { position: relative; width: 899px; height: 1200px; overflow: hidden; }
  .flyer-shapes { position: absolute; inset: 0; }
  .text { position: absolute; white-space: nowrap; }
  .brand { left: 92px; top: 62px; display: flex; align-items: center; gap: 14px; }
  .brand-dot { width: 22px; height: 22px; border-radius: 50%; background: var(--orange); }
  .brand-name { font: 500 60px/1 'Teko', sans-serif; color: var(--orange); letter-spacing: 1px; padding-top: 8px; }
  .save-line { left: 570px; top: 168px; font: 500 53px/1 'Teko', sans-serif; color: var(--ink); letter-spacing: 1px; }
  .save-upto { left: 548px; top: 262px; font: 500 50px/1 'Teko', sans-serif; color: var(--ink); transform: rotate(90deg); transform-origin: center; width: 100px; text-align: center; }
  .save-figure { left: 641px; top: 212px; font: 500 148px/1 'Teko', sans-serif; color: var(--orange); }
  .save-bill { left: 570px; top: 346px; font: 500 54px/1 'Teko', sans-serif; color: var(--ink); }
  .save-bill span { color: var(--orange); }
  .phone { left: 614px; top: 446px; font: 500 42px/1 'Teko', sans-serif; color: var(--ink); letter-spacing: 1px; }
  .warranty { left: 531px; top: 622px; width: 300px; text-align: center; font-family: 'Teko', sans-serif; font-weight: 500; line-height: 0.98; }
  .warranty-years { display: block; font-size: 64px; color: var(--orange); }
  .warranty-word { display: block; font-size: 66px; color: var(--white); }
  .question { right: 47px; font: 900 21px/1 'Lato', sans-serif; color: var(--charcoal-dark); letter-spacing: 3.4px; }
  .q1 { top: 915px; } .q2 { top: 968px; } .q3 { top: 1021px; }
  .solution { left: 0; width: 899px; top: 1082px; text-align: center; font: 400 64px/1 'Teko', sans-serif; color: var(--white); letter-spacing: 0.5px; }
</style>
</head>
<body>
<div class="flyer">
  <svg class="flyer-shapes" width="899" height="1200" viewBox="0 0 899 1200" xmlns="http://www.w3.org/2000/svg">
    <defs>
      <linearGradient id="bg-dark" x1="0" y1="0" x2="0" y2="1">
        <stop offset="0" stop-color="#444"/><stop offset="1" stop-color="#2a2a2a"/>
      </linearGradient>
      <linearGradient id="photo-tones" x1="0" y1="0" x2="1" y2="1">
        <stop offset="0" stop-color="#f4f1ee"/>
        <stop offset="0.5" stop-color="#e2c7b2"/>
        <stop offset="1" stop-color="#8a6a72"/>
      </linearGradient>
    </defs>
    <rect class="backdrop" width="899" height="1200" fill="url(#bg-dark)"/>
    <polygon class="header-stripe" points="0,172 530,160 552,95 899,76 899,94 562,113 538,178 0,192" fill="var(--orange)"/>
    <polygon class="white-panel" points="0,192 538,178 562,113 899,94 899,573 0,785" fill="var(--white)"/>
    <polygon class="photo" role="img" aria-label="Photo of a smiling young man in a plaid shirt fitting an LED bulb into a ceiling socket" points="30,205 500,192 500,625 30,790" fill="url(#photo-tones)" opacity="0.7"/>
    <polygon class="phone-bar" points="570,430 899,430 899,495 543,495" fill="var(--orange)"/>
    <rect class="phone-icon" x="818" y="448" width="30" height="30" rx="5" fill="var(--white)"/>
    <path class="phone-glyph" d="M826 455c2 8 6 13 14 16l3-3-4-3-2 2c-3-2-5-4-7-7l2-2-3-4z" fill="var(--orange)"/>
    <polygon class="box-top" points="0,739 135,785 899,581 899,664 190,996 0,920" fill="var(--orange)"/>
    <polygon class="box-side" points="0,739 135,785 190,996 0,920" fill="var(--orange-deep)"/>
    <polygon class="box-shadow" points="190,996 899,664 899,700 240,1000" fill="#1f1f1f" opacity="0.35"/>
    <circle class="warranty-ring" cx="681" cy="698" r="152" fill="var(--white)"/>
    <circle class="warranty-disc" cx="681" cy="698" r="140" fill="var(--charcoal)"/>
    <polygon class="question-bar" points="372,905 899,905 899,943 344,943" fill="var(--orange)"/>
    <polygon class="question-bar" points="262,958 899,958 899,996 234,996" fill="var(--orange)"/>
    <rect class="question-bar" x="0" y="1011" width="899" height="38" fill="var(--orange)"/>
    <rect class="footer-band" x="0" y="1049" width="899" height="122" fill="var(--charcoal-dark)"/>
    <rect class="footer-stripe" x="0" y="1171" width="899" height="29" fill="var(--orange)"/>
  </svg>

  <div class="text brand"><span class="brand-dot"></span><span class="brand-name">LUMERA LIGHTING</span></div>

  <div class="text save-line">YOU WILL SAVE</div>
  <div class="text save-upto">UP TO</div>
  <div class="text save-figure">90%</div>
  <div class="text save-bill">ELECTRICITY <span>BILL</span></div>

  <div class="text phone">07700900461</div>

  <div class="text warranty">
    <span class="warranty-years">5 YEARS</span>
    <span class="warranty-word">WARRANTY</span>
  </div>

  <div class="text question q1">DO YOU WANT A BETTER LIFE?</div>
  <div class="text question q2">DO YOU WANT TO HELP THE PLANET?</div>
  <div class="text question q3">DO YOU WANT TO SAVE MONEY?</div>

  <div class="text solution">THE LED LIGHT BULBS ARE THE SOLUTION!</div>
</div>
</body>
</html>
```